Sophisticated, clean website reflecting my feminine, playful side to sell my abstract art,

I need a website no more than 3 pages to showcase my paintings, a little about me and some contact info. I do abstracts so looking for something a little edgy, yet feminine and current.
Updates

Hi there, These are some artists websites that I Iike: Mirabelvoss.com (I like how airy it is) tobiasmerrowind.com kevinplodderas.com (I like how it scrolls) I'll need a place for a photo ( a headshot-i do not have it yet so I'll need to be able to upload that later) as well as an area for my bio. Also, it's important that I will be able to upload any new photos and descriptions easily so it should be user friendly. Lastly, I like in a sunny place so would like to have this seem upbeat and playful as that is how i like to paint. thanks-I'm trying to upload my photos now -

Target Market(s)

ppl ages 35-70 who want large scale art for their homes

Industry/Entity Type

art

Coding

Coded - Design and coding required

Number of Pages Required

3 page

Colors

Designer to choose colors to be used in the design.

Requirements
Must have
• photos of my art, a place for my bio, be easy to reach me. tasteful-nothing too "in your face" -my clients are pretty high end and organized. They like clean lines
Nice to have
• sophisticated background, muted tones in the back-similar clean font throughout-no cursive
Should not have
• too many dark areas. Too many blocks of color. Too serious.

```html
<!DOCTYPE html>
<html lang="en">
<head>
<meta charset="utf-8">
<title>Juliet Marrow — Abstract Art</title>
<link rel="stylesheet" href="https://fonts.googleapis.com/css2?family=Archivo:wght@800&family=Montserrat:ital,wght@0,400;0,500;1,400&display=swap">
<style>
  :root {
    --paper: #f3efe7;
    --paper-warm: #f5f1e8;
    --rule: #b9b3aa;
    --ink: #1d1d1d;
    --ink-soft: #2b2b2b;
    --accent: #c08a5a;
    --footer: #dcd1bd;
    --footer-ink: #8a7f72;
    --frame: #f7f4ee;
    --arrow-bg: #ece3d6;
    --arrow-ink: #6e6a64;
    --mark: #1f1f1f;
    --mark-edge: #c7b98f;
    --art-slate: #7f8ba6;
    --art-teal: #2a8a7e;
    --art-navy: #263d72;
  }
  * { box-sizing: border-box; margin: 0; padding: 0; }
  html, body { width: 1152px; height: 1200px; overflow: hidden; }
  body {
    position: relative;
    background: linear-gradient(115deg, #f2eee6 0%, #f5f1ea 45%, #efebe3 100%);
    font-family: "Montserrat", Arial, sans-serif;
    color: var(--ink);
  }
  .site-header {
    position: absolute; left: 0; top: 0; width: 1152px; height: 60px;
    background: var(--paper-warm);
    border-bottom: 1px solid var(--rule);
  }
  .brand-square {
    position: absolute; left: 222px; top: 0; width: 61px; height: 60px;
    background: var(--mark); border: 2px solid var(--mark-edge);
  }
  .brand-name {
    position: absolute; left: 295px; top: 21px;
    font-family: "Archivo", Arial, sans-serif; font-weight: 800;
    font-size: 14px; letter-spacing: 0.2px; color: var(--ink);
  }
  .main-nav a {
    position: absolute; top: 21px; font-size: 13px; font-weight: 400;
    color: var(--ink-soft); text-decoration: none; letter-spacing: 0.3px;
  }
  .nav-about { left: 692px; }
  .nav-gallery { left: 772px; }
  .nav-contact { left: 865px; }

  .column-rule {
    position: absolute; left: 352px; top: 60px; width: 1px; height: 1080px;
    background: var(--rule);
  }

  .slider-frame {
    position: absolute; left: 269px; top: 103px; width: 614px; height: 393px;
    background: var(--frame); border: 1px solid #cfc8bd;
  }
  .slider-artwork {
    position: absolute; left: 4px; top: 4px; width: 606px; height: 383px;
    background: linear-gradient(100deg, var(--art-slate) 0%, var(--art-teal) 50%, var(--art-navy) 100%);
  }
  .slider-arrow {
    position: absolute; top: 283px; width: 32px; height: 58px;
    background: var(--arrow-bg); border-radius: 6px;
  }
  .slider-arrow svg { position: absolute; left: 6px; top: 10px; }
  .arrow-prev { left: 231px; }
  .arrow-next { left: 889px; }
  .slider-caption {
    position: absolute; left: 269px; top: 512px; width: 614px; text-align: center;
    font-size: 13.5px; letter-spacing: 0.2px; color: var(--ink-soft);
  }

  .headshot-ring {
    position: absolute; left: 222px; top: 630px; width: 112px; height: 112px;
    border-radius: 50%; border: 1px solid #cdbfae; background: var(--frame);
  }
  .headshot {
    position: absolute; left: 4px; top: 4px; width: 102px; height: 102px; border-radius: 50%;
    background: linear-gradient(180deg, #1f6668 0%, #2a6a66 45%, #7a4a32 100%);
  }
  .photo-label {
    position: absolute; width: 100%; text-align: center; color: #fff;
    font-size: 9.5px; font-style: italic;
  }
  .headshot .photo-label { top: 55px; }

  .bio { position: absolute; left: 371px; top: 678px; width: 238px; }
  .bio-title { font-size: 13.5px; font-weight: 400; color: var(--accent); letter-spacing: 0.3px; }
  .bio-text {
    margin-top: 16px; font-size: 11px; font-style: italic; line-height: 15.6px; color: var(--ink);
  }
  .bio-text + .bio-text { margin-top: 23px; }
  .follow-link {
    display: inline-block; margin-top: 17px; font-size: 11px; font-style: italic;
    color: var(--accent); text-decoration: underline;
  }
  .social-list { display: flex; gap: 16px; margin-top: 6px; list-style: none; }
  .social-list li {
    width: 21px; height: 21px; border-radius: 50%; background: var(--ink);
    position: relative;
  }
  .social-list svg { position: absolute; left: 5px; top: 6px; }

  .studio-frame {
    position: absolute; left: 680px; top: 632px; width: 212px; height: 312px;
    background: var(--frame); border: 1px solid #cfc8bd;
  }
  .studio-photo {
    position: absolute; left: 3px; top: 3px; width: 204px; height: 304px;
    background: linear-gradient(160deg, #8f8f8d 0%, #a3a19c 35%, #b7ada0 60%, #8a7c6c 100%);
  }
  .studio-photo .photo-label { top: 256px; }

  .site-footer {
    position: absolute; left: 0; top: 1140px; width: 1152px; height: 60px;
    background: var(--footer); border-top: 1px solid var(--rule);
  }
  .copyright {
    position: absolute; left: 0; top: 24px; width: 1182px; text-align: center;
    font-size: 9.5px; color: var(--footer-ink); letter-spacing: 0.2px;
  }
</style>
</head>
<body>
  <header class="site-header">
    <div class="brand-square" aria-hidden="true"></div>
    <div class="brand-name">JULIET MARROW</div>
    <nav class="main-nav">
      <a class="nav-about" href="#">ABOUT</a>
      <a class="nav-gallery" href="#">GALLERY</a>
      <a class="nav-contact" href="#">CONTACT</a>
    </nav>
  </header>

  <div class="column-rule"></div>

  <section class="gallery-slider">
    <div class="slider-frame">
      <div class="slider-artwork" role="img" aria-label="Featured abstract painting by the artist"></div>
    </div>
    <div class="slider-arrow arrow-prev">
      <svg width="20" height="38" viewBox="0 0 20 38"><polyline points="18,1 2,19 18,37" fill="none" stroke="var(--arrow-ink)" stroke-width="1.2"/></svg>
    </div>
    <div class="slider-arrow arrow-next">
      <svg width="20" height="38" viewBox="0 0 20 38"><polyline points="2,1 18,19 2,37" fill="none" stroke="var(--arrow-ink)" stroke-width="1.2"/></svg>
    </div>
    <p class="slider-caption">ABSTRACT ART OF JULIET MARROW</p>
  </section>

  <div class="headshot-ring">
    <div class="headshot" role="img" aria-label="Artist headshot placeholder">
      <span class="photo-label">SAMPLE HEADSHOT</span>
    </div>
  </div>

  <section class="bio">
    <h2 class="bio-title">BIOGRAPHY</h2>
    <p class="bio-text">Lorem ipsum dolor sit amet, consectetur adipiscing elit, sed do eiusmod tempor incididunt ut labore et dolore magna aliqua. Quis ipsum suspendisse ultrices gravida. Risus commodo viverra maecenas accumsan lacus vel facilisis.</p>
    <p class="bio-text">Lorem ipsum dolor sit amet, consectetur adipiscing elit, sed do eiusmod tempor incididunt ut labore et dolore magna aliqua. Quis ipsum suspendisse ultrices gravida. Risus commodo viverra maecenas accumsan lacus vel facilisis.</p>
    <a class="follow-link" href="#">Follow me on Snapfolio</a>
    <ul class="social-list">
      <li aria-label="Snapfolio"></li>
      <li aria-label="Friendwall"></li>
      <li aria-label="Email">
        <svg width="11" height="9" viewBox="0 0 11 9"><rect x="0.5" y="0.5" width="10" height="8" rx="1" fill="#fff"/><polyline points="1,1.5 5.5,5 10,1.5" fill="none" stroke="#1d1d1d" stroke-width="1"/></svg>
      </li>
    </ul>
  </section>

  <div class="studio-frame">
    <div class="studio-photo" role="img" aria-label="Photo of the artist painting at an easel by a window">
      <span class="photo-label">SAMPLE PHOTO</span>
    </div>
  </div>

  <footer class="site-footer">
    <p class="copyright">COPYRGHT 2022 JULIET MARROW ALL RIGHTS RESERVED</p>
  </footer>
</body>
</html>
```